Professional Services/Construction Management (Millwork) Biz Cards

We've decided on a logo and have our color palette set, now we want to design some very professional looking cards that make a strong first impression - they'll reflect our tagline (that we're going to put on the back: Innovative. Professional. Leaders.

The example business card shows generally the direction we've been thinking of going for the back side - **but we're open to other ideas**

Target Market(s)

The cards should target more high-end (wealthy) owners and general contracting companies. We want them to convey a strong first impression - in a professional and not garish way.

Industry/Entity Type

Construction Company

Contact Information for Business Card

There needs to be a place for our company contractor's license number and business address. We want to also have people's names, titles, phone number, email address. The back can be the logo, tagline and web address

Requirements
Must have
• follow our color palette
Nice to have
• Font & Styles should compliment the Harbor Joinery fonts, but not necessarily match exactly

```html
<!DOCTYPE html>
<html lang="en">
<head>
<meta charset="utf-8">
<title>Harbor Joinery Business Cards</title>
<link rel="stylesheet" href="https://fonts.googleapis.com/css2?family=Open+Sans:wght@400;600;700&display=swap">
<style>
  :root {
    --backdrop: #d9d3ca;
    --card-dark: #463c35;
    --card-light: #6e6258;
    --accent-green: #7cc242;
    --text-white: #f2f0ec;
    --text-grey: #b9b2aa;
    --logo-disc: #d6cccb;
    --logo-disc-back: #c9c6c3;
    --logo-ink: #4a4039;
  }
  * { box-sizing: border-box; margin: 0; padding: 0; }
  html, body {
    width: 1200px; height: 1023px; overflow: hidden;
    background: var(--backdrop);
    font-family: "Open Sans", Arial, sans-serif;
  }
  .card {
    position: absolute;
    width: 560px; height: 320px;
    border-radius: 6px;
    background: linear-gradient(135deg, var(--card-light) 0%, var(--card-dark) 70%);
    box-shadow: 0 14px 30px rgba(40, 30, 20, 0.35);
    overflow: hidden;
  }
  .card-front { left: 70px; top: 110px; }
  .card-back { left: 570px; top: 580px; }

  /* Front */
  .brand-block {
    position: absolute; left: 34px; top: 70px; width: 140px;
    text-align: center;
  }
  .brand-disc {
    width: 120px; height: 120px; border-radius: 50%;
    background: var(--logo-disc); margin: 0 auto 12px;
  }
  .brand-name {
    color: var(--accent-green); font-weight: 700; font-size: 15px;
    letter-spacing: 0.5px; text-transform: uppercase;
  }
  .person { position: absolute; left: 210px; top: 44px; }
  .person-name {
    color: var(--accent-green); font-weight: 700; font-size: 22px;
    text-transform: uppercase; letter-spacing: 0.5px;
  }
  .person-title { color: var(--text-white); font-size: 13px; margin-top: 4px; }
  .contact { position: absolute; left: 210px; top: 176px; }
  .contact-line {
    display: flex; align-items: center; gap: 8px;
    color: var(--text-white); font-size: 13px; margin-bottom: 6px;
  }
  .contact-icon {
    width: 14px; height: 14px; border-radius: 2px;
    background: var(--accent-green);
    display: flex; align-items: center; justify-content: center;
  }
  .address {
    color: var(--text-white); font-weight: 700; font-size: 13px;
    text-transform: uppercase; line-height: 1.5; margin-top: 8px;
  }

  /* Back */
  .tagline {
    position: absolute; left: 40px; top: 128px;
    color: var(--accent-green); font-weight: 700; font-size: 19px;
  }
  .website {
    position: absolute; left: 40px; top: 160px;
    color: var(--text-grey); font-size: 13px; letter-spacing: 0.5px;
  }
  .back-emblem {
    position: absolute; right: 34px; top: 80px;
    width: 160px; height: 160px; border-radius: 50%;
    background: var(--logo-disc-back);
    display: flex; align-items: center; justify-content: center;
    text-align: center;
  }
  .back-emblem .brand-name { color: var(--logo-ink); font-size: 16px; line-height: 1.3; }
</style>
</head>
<body>
  <section class="card card-front" aria-label="Business card front">
    <div class="brand-block">
      <div class="brand-disc"></div>
      <div class="brand-name">Harbor Joinery</div>
    </div>
    <div class="person">
      <div class="person-name">Daniel Whitmore</div>
      <div class="person-title">Business Development Manager</div>
    </div>
    <div class="contact">
      <div class="contact-line">
        <span class="contact-icon">
          <svg width="10" height="10" viewBox="0 0 10 10"><path d="M2 1 L4 1 L4.6 3 L3.5 3.8 Q4.5 5.8 6.2 6.5 L7 5.4 L9 6 L9 8 Q5 9 2.5 6.5 Q1 4.5 2 1Z" fill="#463c35"/></svg>
        </span>
        205.555.0148
      </div>
      <div class="contact-line">
        <span class="contact-icon">
          <svg width="10" height="10" viewBox="0 0 10 10"><rect x="1" y="2.5" width="8" height="5.5" fill="none" stroke="#463c35" stroke-width="1"/><path d="M1 2.5 L5 5.5 L9 2.5" fill="none" stroke="#463c35" stroke-width="1"/></svg>
        </span>
        Dan@HarborJoinery.com
      </div>
      <div class="address">
        140 Ridgeline Court, Suite 310<br>
        Maple Falls, AL 35000
      </div>
    </div>
  </section>

  <section class="card card-back" aria-label="Business card back">
    <div class="tagline">Innovative. Professional. Leaders.</div>
    <div class="website">www.HarborJoinery.com</div>
    <div class="back-emblem">
      <div class="brand-name">Harbor<br>Joinery</div>
    </div>
  </section>
</body>
</html>
```